Music Industry Business Needs a Business Card Design

Copper Lantern is an audio mastering company that has been in business for 20 years. Mastering is the final creative step in the music production chain. Our job is to make the music sound as good as it possibly can prior to release to the public. Our world is technical, artistic, precise. We work on everything from independent artists to the music for the Grandfield Cup. We are looking for a new, more modern business card design. I am uploading a copy of our logo, although it doesn't absolutely need to be included in the design.

Target Market(s)

Music Industry Professionals

Industry/Entity Type

Business

Contact Information for Business Card

Address, Phone, Email, Website, Name, Job Title

Font styles to use
Sans Serif

Requirements
Must have
• Sorry, but I don't have any concrete things to request. If I had a clear idea of what I want, I would probably just design something myself. I am looking for fresh input and thought I would try this.
Should not have
• Anything that is typical, such as headphones or the like.

```html
<!DOCTYPE html>
<html lang="en">
<head>
<meta charset="utf-8">
<title>Copper Lantern Mastering – Business Card</title>
<link rel="stylesheet" href="https://fonts.googleapis.com/css2?family=Dosis:wght@400;500;600;700&display=swap">
<style>
  :root {
    --page-bg: #d9d6d2;
    --card-bg: #1d1d1f;
    --text-main: #ffffff;
    --text-muted: #b5b5b8;
    --icon-line: #e6e6e6;
    --font-main: "Dosis", "Arial Narrow", sans-serif;
  }
  html, body {
    margin: 0;
    padding: 0;
    width: 1200px;
    height: 735px;
    overflow: hidden;
    background: var(--page-bg);
    font-family: var(--font-main);
  }
  .card {
    position: absolute;
    left: 110px;
    top: 87px;
    width: 980px;
    height: 560px;
    background: var(--card-bg);
    border-radius: 6px;
    box-shadow: 0 10px 30px rgba(0,0,0,0.25);
    color: var(--text-main);
  }
  .brand {
    position: absolute;
    left: 90px;
    top: 235px;
    display: flex;
    align-items: center;
    gap: 18px;
  }
  .brand-dot {
    width: 26px;
    height: 26px;
    border-radius: 50%;
    background: var(--text-main);
  }
  .brand-name {
    font-size: 46px;
    font-weight: 600;
    letter-spacing: 0.5px;
    text-transform: uppercase;
    color: var(--text-main);
    white-space: nowrap;
  }
  .contact {
    position: absolute;
    right: 70px;
    top: 60px;
    text-align: right;
  }
  .person-name {
    font-size: 34px;
    font-weight: 700;
    line-height: 1;
  }
  .person-title {
    font-size: 19px;
    font-weight: 400;
    color: var(--text-muted);
    margin-top: 2px;
  }
  .contact-row {
    display: flex;
    align-items: center;
    justify-content: flex-end;
    gap: 10px;
  }
  .contact-row.phone {
    margin-top: 34px;
    font-size: 32px;
    font-weight: 600;
  }
  .contact-row.email {
    margin-top: 18px;
    font-size: 26px;
    font-weight: 500;
  }
  .icon {
    width: 32px;
    height: 32px;
    flex: none;
  }
  .address {
    margin-top: 10px;
    font-size: 20px;
    line-height: 1.3;
    color: var(--text-muted);
    font-weight: 400;
  }
  .website {
    position: absolute;
    left: 0;
    right: 0;
    bottom: 48px;
    text-align: center;
    font-size: 34px;
    font-weight: 500;
    letter-spacing: 1px;
  }
</style>
</head>
<body>
  <div class="card">
    <div class="brand">
      <span class="brand-dot"></span>
      <span class="brand-name">Copper Lantern</span>
    </div>

    <div class="contact">
      <div class="person-name">John Doe</div>
      <div class="person-title">Title</div>

      <div class="contact-row phone">
        <svg class="icon" viewBox="0 0 32 32" aria-hidden="true">
          <circle cx="16" cy="16" r="14.5" fill="none" stroke="var(--icon-line)" stroke-width="1.6"/>
          <rect x="11.5" y="8" width="9" height="16" rx="1.5" fill="none" stroke="var(--icon-line)" stroke-width="1.6"/>
          <line x1="14.5" y1="21" x2="17.5" y2="21" stroke="var(--icon-line)" stroke-width="1.4"/>
        </svg>
        <span>(403) 555 - 0187</span>
      </div>

      <div class="contact-row email">
        <svg class="icon" viewBox="0 0 32 32" aria-hidden="true">
          <circle cx="16" cy="16" r="14.5" fill="none" stroke="var(--icon-line)" stroke-width="1.6"/>
          <rect x="9" y="11" width="14" height="10" rx="1" fill="none" stroke="var(--icon-line)" stroke-width="1.6"/>
          <polyline points="9,11.5 16,17 23,11.5" fill="none" stroke="var(--icon-line)" stroke-width="1.6"/>
        </svg>
        <span>john@copperlantern.ca</span>
      </div>

      <div class="address">
        COPPER LANTERN MASTERING<br>
        218 - 7th Avenue N.E.<br>
        Calgary, Alberta, Canada<br>
        T2E 1K5
      </div>
    </div>

    <div class="website">www.copperlantern.ca</div>
  </div>
</body>
</html>
```